Calloway Law - New Letterhead/Logo

Hello!
THE FIRM NAME IS NOW CALLOWAY LAW. We recently just changed our name and we are in need of a classy letterhead. Attached I have a logo we have included in the past, but we are willing to look at other alternatives as well. I will also attach our current letterhead with our old name, Calloway Law. We are willing to go without attorney names. Please help! Thanks
Updates
Project Deadline Extended Reason: Haven't found anything we love Added Tuesday, November 1, 2016

```html
<!DOCTYPE html>
<html lang="en">
<head>
<meta charset="utf-8">
<title>Calloway Law Letterhead</title>
<link href="https://fonts.googleapis.com/css2?family=Cinzel:wght@500&family=Source+Sans+3:wght@400&display=swap" rel="stylesheet">
<style>
  :root {
    --backdrop: #737373;
    --paper: #ffffff;
    --brand-blue: #0b4d8c;
    --ink: #1c1c1c;
    --faint: #e8eaf2;
    --rule: #d9d9d9;
  }
  * { box-sizing: border-box; margin: 0; padding: 0; }
  html, body { width: 1200px; height: 1200px; overflow: hidden; }
  body {
    background: var(--backdrop);
    font-family: "Source Sans 3", sans-serif;
    color: var(--ink);
    position: relative;
  }
  .letterhead {
    position: absolute;
    left: 136px; top: 0;
    width: 927px; height: 1200px;
    background: var(--paper);
  }

  /* masthead */
  .masthead-square {
    position: absolute;
    left: 183px; top: 43px;
    width: 105px; height: 112px;
    background: var(--brand-blue);
  }
  .firm-name {
    position: absolute;
    left: 298px; top: 44px;
    width: 445px; height: 115px;
    font-family: "Cinzel", serif;
    font-weight: 500;
    color: var(--ink);
    text-transform: uppercase;
  }
  .firm-name .line-top {
    position: absolute; left: 0; right: 0; top: 0;
    text-align: center;
    font-size: 30px; line-height: 34px;
    letter-spacing: 11px;
    padding-left: 11px;
  }
  .firm-name .line-of {
    position: absolute; left: 0; right: 0; top: 35px;
    height: 16px;
    text-align: center;
  }
  .firm-name .line-of::before {
    content: "";
    position: absolute; left: 0; right: 0; top: 8px;
    border-top: 1.5px solid var(--ink);
  }
  .firm-name .line-of span {
    position: relative;
    background: var(--paper);
    padding: 0 4px;
    font-size: 17px; line-height: 16px;
  }
  .firm-name .line-main {
    position: absolute; left: 0; right: 0; top: 52px;
    text-align: center;
    font-size: 44px; line-height: 46px;
    letter-spacing: 2px;
  }
  .firm-name .line-llc {
    position: absolute; right: 0; top: 96px;
    font-size: 18px; line-height: 20px;
  }

  /* attorney band */
  .attorney-band {
    position: absolute;
    top: 196px; left: 0; width: 100%; height: 33px;
  }
  .attorney-band svg { position: absolute; inset: 0; }
  .attorney-list {
    position: absolute; inset: 0;
    list-style: none;
    color: #ffffff; font-size: 18px;
  }
  .attorney-list li { position: absolute; top: 5px; line-height: 22px; }
  .attorney-list li::before { content: "\2022"; margin-right: 3px; }

  /* faint name in the body */
  .faint-mark {
    position: absolute;
    top: 500px; left: 0; right: 0;
    text-align: center;
    color: var(--faint);
    font-family: "Cinzel", serif;
    font-weight: 500;
    font-size: 112px;
    line-height: 140px;
    text-transform: uppercase;
  }

  /* footer */
  .contact {
    position: absolute;
    top: 1108px; left: 22px;
    font-size: 18px; line-height: 22px;
  }
  .contact-row { display: flex; }
  .contact-row dt { width: 76px; }
  .contact-row a { color: var(--brand-blue); text-decoration: none; }
  .address {
    position: absolute;
    top: 1108px; right: 22px;
    text-align: right;
    font-size: 18px; line-height: 22px;
    font-style: normal;
  }
</style>
</head>
<body>
  <main class="letterhead">
    <header class="masthead">
      <div class="masthead-square"></div>
      <div class="firm-name">
        <span class="line-top">Law Offices</span>
        <span class="line-of"><span>of</span></span>
        <span class="line-main">Calloway Law</span>
        <span class="line-llc">LLC</span>
      </div>
    </header>

    <div class="attorney-band">
      <svg width="927" height="33" viewBox="0 0 927 33">
        <line x1="0" y1="0.5" x2="927" y2="0.5" stroke="var(--rule)" stroke-width="1"/>
        <line x1="0" y1="32.5" x2="927" y2="32.5" stroke="var(--rule)" stroke-width="1"/>
        <polygon points="0,0 912,0 929,16.5 912,33 0,33" fill="var(--brand-blue)" transform="translate(-17 0)"/>
      </svg>
      <ul class="attorney-list">
        <li style="left:127px">Daniel W. Calloway, Esq.</li>
        <li style="left:358px">Martin E. Ashford, Esq.</li>
        <li style="left:602px">Peter D. Vanlandt, Esq.</li>
      </ul>
    </div>

    <div class="faint-mark" aria-hidden="true">Calloway<br>Law</div>

    <dl class="contact">
      <div class="contact-row"><dt>Phone</dt><dd>: (303) 555-0143</dd></div>
      <div class="contact-row"><dt>&nbsp;Fax</dt><dd>: (303) 555-0187</dd></div>
      <div class="contact-row"><dt>Web</dt><dd>: <a href="#">www.callowaylegal.net</a></dd></div>
    </dl>

    <address class="address">
      4120 Meridian Parkway<br>
      Suite 620<br>
      Cherry Hills, Colorado 80113
    </address>
  </main>
</body>
</html>
```